Business Card Design Project

Please create a custom business card for Birchmoor Links School. The logo is attached to this brief.

Colours could be based on Blue, black, red, or white color. Colors like orange, green, purple, pink are not preferable.

Here is the link to the logo project : http://tasks.artquarrel.net/task.aspx?id=413057

Questions can be posted on the Discussion Board.

```html
<!DOCTYPE html>
<html lang="en">
<head>
<meta charset="utf-8">
<title>Birchmoor Links School — Business Card</title>
<link rel="stylesheet" href="https://fonts.googleapis.com/css2?family=Open+Sans:wght@400;600;700&display=swap">
<style>
  :root {
    --navy-deep: #141a5a;
    --navy: #1f2a7e;
    --navy-glow: #2a3796;
    --white: #ffffff;
    --silver: #c9ccd6;
    --silver-dark: #9a9eab;
    --page: #e9e9ec;
  }
  * { box-sizing: border-box; margin: 0; padding: 0; }
  html, body { width: 1200px; height: 900px; overflow: hidden; }
  body {
    background: var(--page);
    font-family: "Open Sans", sans-serif;
    position: relative;
  }
  .card {
    position: absolute;
    left: 320px;
    width: 560px;
    height: 320px;
    border-radius: 22px;
    overflow: hidden;
    box-shadow: 0 6px 18px rgba(0,0,0,0.18);
  }
  .card--front { top: 100px; background: var(--white); }
  .card--back {
    top: 480px;
    background: radial-gradient(ellipse at 55% 45%, var(--navy-glow) 0%, var(--navy) 45%, var(--navy-deep) 100%);
  }
  .front-art { position: absolute; inset: 0; }
  .contact {
    position: absolute;
    left: 38px;
    top: 36px;
    color: var(--white);
  }
  .contact__name {
    font-weight: 600;
    font-size: 17px;
    letter-spacing: 0.5px;
    text-transform: uppercase;
  }
  .contact__title { font-size: 12px; margin-top: 2px; opacity: 0.9; }
  .contact__address { font-size: 12px; margin-top: 14px; line-height: 1.35; }
  .contact__list { list-style: none; margin-top: 12px; font-size: 12.5px; }
  .contact__list li { display: flex; align-items: center; gap: 8px; line-height: 1.55; }
  .contact__list svg { width: 12px; height: 12px; flex: none; }
  .brand {
    position: absolute;
    display: flex;
    align-items: center;
    gap: 12px;
    font-weight: 700;
  }
  .brand__dot { border-radius: 50%; flex: none; }
  .brand__name { line-height: 1.05; }
  .brand--front {
    right: 26px;
    top: 132px;
    width: 200px;
    color: var(--navy-deep);
    font-size: 22px;
  }
  .brand--front .brand__dot { width: 34px; height: 34px; background: var(--navy-deep); }
  .brand--back {
    left: 0; right: 0;
    top: 120px;
    justify-content: center;
    color: var(--white);
    font-size: 32px;
  }
  .brand--back .brand__dot { width: 46px; height: 46px; background: var(--white); }
  .website {
    position: absolute;
    left: 0; right: 0;
    top: 200px;
    text-align: center;
    color: var(--white);
    font-size: 16px;
    letter-spacing: 2px;
  }
</style>
</head>
<body>

<section class="card card--front" aria-label="Business card front">
  <svg class="front-art" viewBox="0 0 560 320" preserveAspectRatio="none" aria-hidden="true">
    <defs>
      <linearGradient id="navyPanel" x1="0" y1="0" x2="1" y2="1">
        <stop offset="0" stop-color="#2a3796"/>
        <stop offset="1" stop-color="#141a5a"/>
      </linearGradient>
      <linearGradient id="silverBand" x1="0" y1="0" x2="0" y2="1">
        <stop offset="0" stop-color="#e6e8ee"/>
        <stop offset="0.5" stop-color="#9a9eab"/>
        <stop offset="1" stop-color="#d4d6de"/>
      </linearGradient>
    </defs>
    <rect width="560" height="320" fill="url(#navyPanel)"/>
    <path d="M330 0 Q 300 10 292 90 Q 282 200 305 320 L560 320 L560 0 Z" fill="url(#silverBand)"/>
    <path d="M350 0 Q 320 15 314 95 Q 306 200 325 320 L560 320 L560 0 Z" fill="#1f2a7e"/>
    <path d="M366 0 Q 334 20 330 100 Q 324 200 342 320 L560 320 L560 0 Z" fill="#ffffff"/>
  </svg>

  <div class="contact">
    <p class="contact__name">Owen Callard</p>
    <p class="contact__title">Manager</p>
    <p class="contact__address">4180 Larkfield Rd<br>Hollisford TX 75500</p>
    <ul class="contact__list">
      <li><svg viewBox="0 0 12 12"><path d="M2 1h2.5l1 3-1.5 1a6 6 0 0 0 3 3l1-1.5 3 1V10a1 1 0 0 1-1 1A9 9 0 0 1 1 2a1 1 0 0 1 1-1z" fill="#fff"/></svg>512 404 2270</li>
      <li><svg viewBox="0 0 12 12"><rect x="2.5" y="1" width="7" height="10" rx="1.2" fill="#fff"/></svg>512 404 2271</li>
      <li><svg viewBox="0 0 12 12"><rect x="0.5" y="2" width="11" height="8" rx="1" fill="#fff"/><path d="M1 2.5l5 4 5-4" stroke="#1f2a7e" fill="none"/></svg>info@BirchmoorLinksSchool.com</li>
      <li><svg viewBox="0 0 12 12"><circle cx="6" cy="6" r="5" fill="none" stroke="#fff" stroke-width="1.3"/><path d="M1 6h10M6 1c2.5 3 2.5 7 0 10M6 1c-2.5 3-2.5 7 0 10" stroke="#fff" fill="none"/></svg>www.BirchmoorLinksSchool.com</li>
    </ul>
  </div>

  <div class="brand brand--front">
    <span class="brand__dot"></span>
    <span class="brand__name">Birchmoor Links School</span>
  </div>
</section>

<section class="card card--back" aria-label="Business card back">
  <div class="brand brand--back">
    <span class="brand__dot"></span>
    <span class="brand__name">Birchmoor Links School</span>
  </div>
  <p class="website">www.BirchmoorLinksSchool.com</p>
</section>

</body>
</html>
```